Adjust children's activity materials to branding and theme

Hello, we are a global kindergarten (nursery) chain and would like to provide branded printable activity sheets for our schools around the world, that would also reflect the theme of the curriculum.
We can provide the activity sheets that then need to be converted to our style and branded with our logo, colours and branding elements and include an item that reflects the theme, in our visual style. A full branding and colour codes guide is available for the chosen artist.

The 'grapheme' booklet attachment is provided as an example, please let us know how many similar pages you would be able to process within the budget. Each page is a standalone design task and can be printed out individually or as a booklet.

Industry/Entity Type

Early Education

Requirements
Must have
• BrightNest branding

```html
<!DOCTYPE html>
<html lang="en">
<head>
<meta charset="utf-8">
<title>Happy Lunar New Year – BrightNest</title>
<link rel="stylesheet" href="https://fonts.googleapis.com/css2?family=Bebas+Neue&family=Fredoka:wght@600&display=swap">
<style>
  :root {
    --paper: #f2eeeb;
    --teal: #4ba2a8;
    --plum: #8e4a68;
    --red: #d9282d;
    --coral: #e0544a;
    --yellow: #f8d95c;
    --blossom-green: #6fa9a0;
  }
  html, body {
    margin: 0;
    padding: 0;
    width: 848px;
    height: 1200px;
    overflow: hidden;
    background: var(--paper);
  }
  .cover {
    position: relative;
    width: 848px;
    height: 1200px;
    background: var(--paper);
    overflow: hidden;
  }
  .cover__shapes {
    position: absolute;
    inset: 0;
  }
  .cover__title {
    position: absolute;
    left: 62px;
    top: 188px;
    margin: 0;
    font-family: "Bebas Neue", "Oswald", sans-serif;
    font-weight: 400;
    font-size: 150px;
    line-height: 122px;
    letter-spacing: 2px;
    color: var(--teal);
  }
  .cover__title span { display: block; }
  .cover__from {
    position: absolute;
    left: 66px;
    top: 880px;
    margin: 0;
    font-family: "Fredoka", "Nunito", sans-serif;
    font-weight: 600;
    font-size: 40px;
    line-height: 54px;
    color: var(--teal);
  }
  .cover__from span { display: block; }
  .art {
    position: absolute;
  }
  .art--blossom {
    right: 0;
    top: 0;
    width: 190px;
    height: 470px;
    border-radius: 0 0 0 120px;
    background: linear-gradient(200deg, rgba(217,40,45,0.55), rgba(111,169,160,0.35) 60%, rgba(242,238,235,0) 100%);
  }
  .art--cloud {
    left: 66px;
    top: 740px;
    width: 330px;
    height: 110px;
    border-radius: 60px;
    background: var(--plum);
    opacity: 0.85;
  }
  .art--lion-dance {
    right: 0;
    bottom: 0;
    width: 470px;
    height: 560px;
    border-radius: 200px 0 0 0;
    background: radial-gradient(ellipse at 60% 35%, #e0544a 0%, #d9282d 35%, #f0b64a 70%, rgba(240,182,74,0.4) 100%);
  }
  .art--flowers {
    left: 40px;
    bottom: 0;
    width: 380px;
    height: 95px;
    border-radius: 50px 50px 0 0;
    background: linear-gradient(90deg, var(--red), var(--plum) 50%, var(--red));
  }
</style>
</head>
<body>
  <main class="cover">
    <svg class="cover__shapes" width="848" height="1200" viewBox="0 0 848 1200" aria-hidden="true">
      <polygon class="corner-tab" points="0,0 165,0 0,145" fill="var(--yellow)"/>
      <polygon class="accent-panel" points="848,570 848,1200 560,1200 390,1020" fill="var(--teal)"/>
    </svg>

    <div class="art art--blossom" role="img" aria-label="Plum blossom branch with red petals and a hanging red paper lantern"></div>

    <h1 class="cover__title">
      <span>Happy</span>
      <span>Lunar</span>
      <span>New</span>
      <span>Year</span>
    </h1>

    <div class="art art--cloud" role="img" aria-label="Plum-coloured auspicious cloud ornament with gold swirls"></div>

    <p class="cover__from">
      <span>FROM</span>
      <span>BrightNest</span>
    </p>

    <div class="art art--lion-dance" role="img" aria-label="Illustration of two children performing a red lion dance"></div>

    <div class="art art--flowers" role="img" aria-label="Row of red and plum decorative flowers"></div>
  </main>
</body>
</html>
```